RK Bastone Construction Inc.

Design a new business card for our construction company
To be removed from current card:
Delete 25 years
Delete Tenant fit up Renovations section

```html
<!DOCTYPE html>
<html lang="en">
<head>
<meta charset="utf-8">
<title>RK Bastone Construction Inc. – Business Card</title>
<link href="https://fonts.googleapis.com/css2?family=Montserrat:wght@800&family=Didact+Gothic&display=swap" rel="stylesheet">
<style>
  :root {
    --bg: #e6e6e8;
    --card: #ffffff;
    --purple: #4b2a6e;
    --teal: #1f7668;
    --ink: #3a3a3a;
    --ghost: rgba(75, 42, 110, 0.08);
  }
  * { margin: 0; padding: 0; box-sizing: border-box; }
  html, body {
    width: 1200px; height: 900px; overflow: hidden;
    background: var(--bg);
  }
  .canvas { position: relative; width: 1200px; height: 900px; }
  .card {
    position: absolute; left: 270px;
    width: 660px; height: 377px;
    background: linear-gradient(135deg, #ffffff 0%, #f3f3f4 100%);
    box-shadow: 0 8px 24px rgba(0,0,0,0.12);
    overflow: hidden;
  }
  .card--front { top: 50px; }
  .card--back { top: 473px; }

  .wordmark {
    position: absolute;
    font-family: "Montserrat", sans-serif;
    font-weight: 800;
    color: var(--purple);
    line-height: 1.05;
    letter-spacing: 0.5px;
    text-transform: uppercase;
  }
  .wordmark__main { display: block; font-size: 40px; }
  .wordmark__sub { display: block; font-size: 19px; letter-spacing: 3px; }

  .card--front .wordmark { left: 250px; top: 175px; }
  .card--back .wordmark { left: 34px; top: 34px; }

  .ghost-mark {
    position: absolute;
    font-family: "Montserrat", sans-serif;
    font-weight: 800;
    color: var(--ghost);
    text-transform: uppercase;
    white-space: nowrap;
    line-height: 1;
    writing-mode: vertical-rl;
  }
  .ghost-mark__main { font-size: 46px; }
  .ghost-mark__sub { font-size: 20px; letter-spacing: 3px; }
  .card--front .ghost-mark { left: 0; bottom: 10px; transform: rotate(180deg); }
  .card--back .ghost-mark { right: 0; top: 10px; }

  .person { position: absolute; left: 34px; top: 190px; }
  .person__name {
    font-family: "Montserrat", sans-serif; font-weight: 800;
    font-size: 20px; color: var(--purple); text-transform: uppercase;
    letter-spacing: 0.5px;
  }
  .contact-list {
    list-style: none;
    font-family: "Didact Gothic", sans-serif;
    font-size: 16px; color: var(--ink);
  }
  .contact-list li { display: flex; align-items: center; gap: 10px; height: 26px; }
  .contact-list svg { width: 16px; height: 16px; flex: none; }
  .contact-list--mobile { margin-top: 6px; }
  .contact-list--office { margin-top: 24px; }

  .address {
    position: absolute; left: 360px; top: 218px;
    display: flex; gap: 10px;
    font-family: "Didact Gothic", sans-serif; font-size: 16px; color: var(--ink);
    line-height: 1.5;
  }
  .address svg { width: 16px; height: 20px; flex: none; margin-top: 3px; }
</style>
</head>
<body>
<main class="canvas">

  <section class="card card--front" aria-label="Business card front">
    <div class="ghost-mark" aria-hidden="true">
      <span class="ghost-mark__main">RK Bastone</span>
      <span class="ghost-mark__sub">Construction Inc.</span>
    </div>
    <h1 class="wordmark">
      <span class="wordmark__main">RK Bastone</span>
      <span class="wordmark__sub">Construction Inc.</span>
    </h1>
  </section>

  <section class="card card--back" aria-label="Business card back">
    <div class="ghost-mark" aria-hidden="true">
      <span class="ghost-mark__main">RK Bastone</span>
      <span class="ghost-mark__sub">Construction Inc.</span>
    </div>
    <h2 class="wordmark">
      <span class="wordmark__main">RK Bastone</span>
      <span class="wordmark__sub">Construction Inc.</span>
    </h2>

    <div class="person">
      <p class="person__name">Marco Bastone</p>
      <ul class="contact-list contact-list--mobile">
        <li>
          <svg viewBox="0 0 16 16" aria-hidden="true"><rect x="4" y="1" width="8" height="14" rx="1.5" fill="none" stroke="var(--teal)" stroke-width="1.4"/><circle cx="8" cy="12.5" r="0.8" fill="var(--teal)"/></svg>
          613-555-0142
        </li>
      </ul>
      <ul class="contact-list contact-list--office">
        <li>
          <svg viewBox="0 0 16 16" aria-hidden="true"><path d="M1 6 Q8 1 15 6 L13 8 L11 6.5 V5 H5 V6.5 L3 8 Z" fill="var(--teal)"/><rect x="3" y="9" width="10" height="5" rx="1" fill="var(--teal)"/></svg>
          613-555-0187 ext.221
        </li>
        <li>
          <svg viewBox="0 0 16 16" aria-hidden="true"><rect x="1.5" y="3.5" width="13" height="9" rx="1" fill="none" stroke="var(--teal)" stroke-width="1.4"/><path d="M1.5 4 L8 9 L14.5 4" fill="none" stroke="var(--teal)" stroke-width="1.4"/></svg>
          marco@rkbastoneconstruction.ca
        </li>
        <li>
          <svg viewBox="0 0 16 16" aria-hidden="true"><circle cx="8" cy="8" r="6.3" fill="none" stroke="var(--teal)" stroke-width="1.4"/><ellipse cx="8" cy="8" rx="2.8" ry="6.3" fill="none" stroke="var(--teal)" stroke-width="1.1"/><path d="M1.7 8 H14.3" stroke="var(--teal)" stroke-width="1.1"/></svg>
          www.rkbastoneconstruction.ca
        </li>
      </ul>
    </div>

    <address class="address">
      <svg viewBox="0 0 16 20" aria-hidden="true"><path d="M8 1 C4 1 1.5 4 1.5 7.3 C1.5 12 8 19 8 19 C8 19 14.5 12 14.5 7.3 C14.5 4 12 1 8 1 Z" fill="var(--teal)"/><circle cx="8" cy="7.3" r="2.4" fill="#fff"/></svg>
      <span>2180 Ridgeline Rd. Suite 100<br>Ottawa, ON K1B4T7</span>
    </address>
  </section>

</main>
</body>
</html>
```